7th Annual Falcon Ridge Classic Flyer

Looking to design an updated eye catching flyer maybe with someone movement, sound, and color. Below is an attachment of the flyer I have used in the past. I need to add color, sound, and movement to the flyer. This is an advertisement for youth folk style wrestling. You may contact me directly at 252-381-4927 if you need additional information. I really like the colors music and movement in the video below.
https://www.vidloomer.com/watch?v=kQ7mTbLw2Ra

Target Market(s)

Youth Wrestling

Font styles to use
Serif

Colors
EB3D1F
EC4F4E
F09395
F8D3D4
FCEDEE

Requirements
Must have
• All information included on flyer.
Nice to have
• Color, sound, and movement

```html
<!DOCTYPE html>
<html lang="en">
<head>
<meta charset="utf-8">
<title>Falcon Ridge Classic – Weigh-ins &amp; Info</title>
<link rel="stylesheet" href="https://fonts.googleapis.com/css2?family=Source+Serif+4:opsz,wght@8..60,400;8..60,600;8..60,700&display=swap">
<style>
  :root {
    --red: #eb3d1f;
    --coral: #ec4f4e;
    --pink: #f09395;
    --blush: #f8d3d4;
    --shell: #fcedee;
    --ink: #4a1712;
    --white: #ffffff;
  }
  html, body { margin: 0; padding: 0; overflow: hidden; background: var(--shell); }
  .flyer {
    position: relative;
    width: 848px;
    height: 1200px;
    overflow: hidden;
    background: var(--shell);
    font-family: "Source Serif 4", serif;
    color: var(--ink);
  }
  .backdrop { position: absolute; inset: 0; width: 848px; height: 1200px; }
  .band { animation: drift 6s ease-in-out infinite alternate; }
  .band-left { animation-delay: -3s; }
  .emblem-glow { animation: glow 5s ease-in-out infinite alternate; transform-origin: 300px 450px; }
  @keyframes drift {
    from { transform: translateX(0); }
    to   { transform: translateX(8px); }
  }
  @keyframes glow {
    from { opacity: 0.75; transform: scale(1); }
    to   { opacity: 1; transform: scale(1.04); }
  }
  @keyframes pulse {
    from { box-shadow: 0 0 0 0 rgba(235, 61, 31, 0.45); }
    to   { box-shadow: 0 0 0 12px rgba(235, 61, 31, 0); }
  }
  .content { position: absolute; inset: 0; }
  .weighins { position: absolute; left: 29px; top: 24px; width: 780px; }
  .weighins h2 {
    margin: 0 0 10px; font-size: 26px; font-weight: 700; color: var(--red);
  }
  .weighins p { margin: 0; font-size: 17.5px; line-height: 34px; font-weight: 400; }
  .weighins .early { margin-bottom: 12px; }
  .admission {
    position: absolute; left: 29px; top: 409px;
    width: 400px; height: 58px; border-radius: 29px;
    background: var(--red); color: var(--white);
    display: flex; align-items: center; justify-content: center;
    font-size: 23px; font-weight: 700;
    animation: pulse 1.8s ease-out infinite;
  }
  .contact {
    position: absolute; left: 29px; top: 505px;
    margin: 0; font-size: 24px; line-height: 34px; font-weight: 400;
    color: var(--ink);
  }
  .contact .phone { color: var(--coral); font-weight: 600; }
  .hotels { position: absolute; left: 500px; top: 617px; }
  .hotels h3 { margin: 0 0 8px; font-size: 24px; font-weight: 700; color: var(--red); }
  .hotels ul { list-style: none; margin: 0; padding: 0; }
  .hotels li { font-size: 20px; line-height: 40px; }
  @media (prefers-reduced-motion: reduce) {
    .band, .emblem-glow, .admission { animation: none; }
  }
</style>
</head>
<body>
<div class="flyer">
  <svg class="backdrop" viewBox="0 0 595 842" xmlns="http://www.w3.org/2000/svg">
    <defs>
      <radialGradient id="crestGlow" cx="50%" cy="45%" r="55%">
        <stop offset="0" stop-color="#f09395" stop-opacity="0.55"/>
        <stop offset="0.6" stop-color="#f8d3d4" stop-opacity="0.6"/>
        <stop offset="1" stop-color="#fcedee" stop-opacity="0"/>
      </radialGradient>
    </defs>
    <rect width="595" height="842" fill="#fcedee"/>
    <g role="img" aria-label="Faint large warrior helmet emblem behind the text">
      <ellipse class="emblem-glow" cx="300" cy="450" rx="230" ry="420" fill="url(#crestGlow)"/>
    </g>
    <polyline class="band band-right" points="575,-20 388,237 600,455" fill="none" stroke="#f09395" stroke-width="42" stroke-opacity="0.75"/>
    <polyline class="band band-left" points="-20,405 205,630 -15,850" fill="none" stroke="#ec4f4e" stroke-width="42" stroke-opacity="0.85"/>
  </svg>

  <div class="content">
    <section class="weighins">
      <h2>Weigh-ins</h2>
      <p class="early">January 24, 2025 – 5:00 pm to 7:00 pm (Early Weigh-ins - $10 cash due at scale)</p>
      <p>January 25, 2025 – 6:00 am to 7:30 am (4U, 6U, 8U, 10U)</p>
      <p>January 25, 2025 – 11:00 am to 12:00 pm (12 &amp; Under, MS, &amp; High School)</p>
      <p>Tenths are waived/dropped at weigh-ins. Satellite weigh-ins will not be allowed.</p>
      <p>High School Divisions are given 2 lbs. growth allowance.</p>
      <p>Custom medals will be given to the top 3 individual finishers in each bracket.</p>
      <p>Custom Awards will be awarded to the top 4 teams. Referee decisions will be final.</p>
      <p>Pine Hollow Athletics is not responsible for accidents, injuries, or theft during the<br>tournament.</p>
    </section>

    <div class="admission">Admission:&nbsp; $10.00 per person</div>

    <p class="contact">For More Information, contact Tournament Director Dale Corwin:<br><span class="phone">252-381-4927</span></p>

    <section class="hotels">
      <h3>Hotels Available On-Site</h3>
      <ul>
        <li>Larkspur Suites (252) 610-2200</li>
        <li>Meadowbrook Inn (252) 610-4700</li>
        <li>Riverstone Lodge (252) 610-8300</li>
      </ul>
    </section>
  </div>
</div>
</body>
</html>
```